Occupational Therapy Clinic Advertisement

Create an advertisement for a magazine. Below I have attached my original ad (Ad 2020.pdf) . I want the ad changed and it should be eye catching. I would like a eye catching graphics added in the ad. It should be a graphic image that applies to education. I am attaching a sample graphic image of that I liked from someone elses ad- it should not be the same- it just is there to show what I like. Please use the same words from my original ad.Dimensions: 3.75in x 10.3 in

Target Market(s)

Parents of School aged children

Requirements
Must have
• Must have eye catching Graphic. Colors should be eye catching for a typed magazine.

```html
<!DOCTYPE html>
<html lang="en">
<head>
<meta charset="utf-8">
<title>Gentle Steps OT Services – Magazine Ad</title>
<link rel="stylesheet" href="https://fonts.googleapis.com/css2?family=Montserrat:wght@400;500&family=Poppins:wght@700;800&display=swap">
<style>
  :root {
    --blue: #0f67dd;
    --blue-soft: #8cc2f6;
    --strike: #e2574c;
    --yellow: #f8f46a;
    --yellow-pale: #f8f7b3;
    --row-blue: #e3edfa;
    --white: #ffffff;
    --art-warm: #f2d3e6;
    --art-cool: #cfe3ef;
  }
  * { margin: 0; padding: 0; box-sizing: border-box; }
  html, body { width: 1200px; height: 3297px; overflow: hidden; background: var(--white); }
  .ad { position: relative; width: 1200px; height: 3297px; background: var(--white); color: var(--blue); font-family: "Montserrat", sans-serif; }
  .abs { position: absolute; }

  .hero-art { left: 50px; top: 186px; width: 510px; height: 450px; border-radius: 30px;
    background: linear-gradient(135deg, var(--art-warm), #e6d3f2 55%, #d9d0ea); }
  .headline { right: 58px; top: 104px; text-align: right; font-family: "Poppins", sans-serif; font-weight: 800;
    font-size: 96px; line-height: 102px; letter-spacing: -2px; white-space: nowrap; }
  .headline .can { color: var(--blue-soft); position: relative; }
  .headline .can::after { content: ""; position: absolute; left: -4px; right: -18px; top: 48%; height: 8px;
    background: var(--strike); transform: rotate(-4deg); border-radius: 4px; }

  .band { left: 0; width: 1200px; }
  .band-yellow { background: var(--yellow); }
  .band-blue { background: var(--row-blue); }

  .kids-art { left: 41px; top: 898px; width: 430px; height: 470px; border-radius: 24px;
    background: linear-gradient(160deg, #f6e0cc, #cfe6ef 60%, #c7a98a); }
  .question-title { left: 514px; top: 858px; font-family: "Poppins", sans-serif; font-weight: 800; font-size: 50px; }
  .rule { height: 7px; background: var(--blue); }
  .questions { left: 512px; top: 985px; width: 640px; list-style: none; font-size: 36px; line-height: 59px; letter-spacing: 0.5px; }
  .questions li { margin-bottom: 58px; }

  .fact { display: flex; align-items: center; font-size: 34px; }
  .fact .label { position: absolute; left: 105px; }
  .fact .sep { position: absolute; left: 378px; }
  .fact .value { position: absolute; left: 447px; }
  .tagline { display: flex; align-items: center; justify-content: center; font-size: 46px; letter-spacing: 0.5px; }

  .activity-art { left: 91px; top: 2019px; width: 324px; height: 560px;
    background: linear-gradient(180deg, #a8cde0, #9fc3d8 45%, #6b2a4a 100%); }
  .brand-name { left: 463px; top: 2130px; font-family: "Poppins", sans-serif; font-weight: 800; font-size: 88px; }
  .brand-sub { left: 465px; top: 2256px; font-family: "Poppins", sans-serif; font-weight: 800; font-size: 36px; }
  .brand-phone { left: 463px; top: 2384px; font-size: 54px; }

  .info-box { left: 54px; top: 2703px; width: 1091px; height: 225px; background: var(--yellow-pale);
    text-align: center; font-family: "Poppins", sans-serif; font-weight: 800; font-size: 35px; line-height: 42px; padding-top: 26px; }
  .info-box .gap { margin-top: 38px; }
  .contact-note { left: 0; width: 1200px; top: 2966px; text-align: center; font-family: "Poppins", sans-serif; font-weight: 800; font-size: 38px; line-height: 42px; }
  .contact-note a { color: var(--blue); text-decoration: underline; }
  .signature { left: 0; width: 1200px; top: 3082px; text-align: center; font-family: "Poppins", sans-serif; font-weight: 800; }
  .signature .name { font-size: 60px; line-height: 78px; }
  .signature .phone { font-size: 54px; line-height: 60px; }
</style>
</head>
<body>
<main class="ad">
  <div class="abs hero-art" role="img" aria-label="Illustration of a girl reading and a teacher building a robot"></div>
  <h1 class="abs headline">YES, YOUR<br>CHILD <span class="can">CAN</span><br>WILL<br>SUCCEED IN<br>SCHOOL!</h1>

  <div class="abs band band-yellow" style="top:712px;height:125px"></div>

  <div class="abs kids-art" role="img" aria-label="Illustration of two children playing with a bead maze at a table"></div>
  <h2 class="abs question-title">Does your child?</h2>
  <div class="abs rule" style="left:514px;top:941px;width:121px"></div>
  <ul class="abs questions">
    <li>Struggle with Reading/Kriah?</li>
    <li>Knows the Information but<br>fails the test?</li>
    <li>Has difficulty remembering<br>names and dates?</li>
  </ul>

  <div class="abs band band-blue fact" style="top:1445px;height:116px"><span class="label">We Evaluate</span><span class="sep">|</span><span class="value">Using Standardized tests</span></div>
  <div class="abs band band-yellow fact" style="top:1577px;height:116px"><span class="label">We Treat</span><span class="sep">|</span><span class="value">Using Research based techniques</span></div>
  <div class="abs band band-blue fact" style="top:1711px;height:115px"><span class="label">Ages</span><span class="sep">|</span><span class="value">6-18</span></div>
  <div class="abs band band-yellow tagline" style="top:1846px;height:115px">We treat the underlying processing deficits</div>

  <div class="abs activity-art" role="img" aria-label="Collage illustration of children playing, climbing and doing crafts"></div>
  <div class="abs brand-name">Gentle Steps</div>
  <div class="abs brand-sub">OT Services</div>
  <div class="abs rule" style="left:463px;top:2337px;width:124px"></div>
  <div class="abs brand-phone">(718) 555-0142</div>

  <div class="abs band band-yellow" style="top:2645px;height:652px"></div>
  <div class="abs info-box">
    <p>Located in Borough Park</p>
    <p>Evaluations done in Borough Park and Staten Island</p>
    <p class="gap">Board of Ed OT RSA's accepted</p>
  </div>
  <p class="abs contact-note">For more information or to join our email list, drop an<br>email at <a href="mailto:gentlestepsot@example.com">gentlestepsot@example.com</a></p>
  <div class="abs signature">
    <p class="name">Miriam Kessler OTR/L</p>
    <p class="phone">(718) 555-0142</p>
  </div>
</main>
</body>
</html>
```